Design for Cedar Lark Homes real estate agency

Incorporate logo into new business cards. I need to include the Brindley Vance logo incorporated into Cedar Lark Homes on one side of the card (attached). On the other side I see just the icon with "Maren Quill" (attached) with "Rooted in Trust" either included as is or removed from logo and rather put as a tag line on the business card separate from the main logo. Contact information:

Maren Quill
Associate Broker
Cell: 730-418-5093
Email: marenquill@cedarlarkhomes.example
Web: www.cedarlarkhomes.example

Target Market(s)

Buyers, Sellers, Builders and Investors of homes and land

Industry/Entity Type

Real Estate Agent

Contact Information for Business Card

My client base tend to be higher end home buyers, sellers, builders and investors. I have been more and more in land and subdivisions for builders and investors. The card should not be cluttered. Clean and simple - yet with an air of exclusive/high end

Colors

Designer to choose colors to be used in the design.

Requirements
Must have
• Must have the logo on one side that has Brindley Vance logo incorporated. The side that has my contact information does not have to have the Brindley Vance logo incorporated.
• Must include "Rooted in Trust" tag line either within logo (as is) or removed from logo and included in another position on the side of the business card with contact information.
Should not have
• Should not have Brindley Vance logo incorporated into Cedar Lark Homes logo on both sides of business card. Would like the Cedar Lark Homes logo that has Brindley Logo only on the back side of card without contact information.

```html
<!DOCTYPE html>
<html lang="en">
<head>
<meta charset="utf-8">
<title>Cedar Lark Homes – Business Cards</title>
<link rel="stylesheet" href="https://fonts.googleapis.com/css2?family=Encode+Sans+Condensed:wght@500;700&family=Open+Sans:wght@400;600&family=Playfair+Display:wght@400&display=swap">
<style>
  :root {
    --bg: #e4e5e7;
    --paper: #ffffff;
    --brown: #5a3a0e;
    --gold: #d9b21c;
    --gold-light: #e9c52a;
    --ink: #1e1a14;
    --muted: #7a6a52;
  }
  * { box-sizing: border-box; margin: 0; padding: 0; }
  html, body { width: 1200px; height: 800px; overflow: hidden; }
  body {
    background: var(--bg);
    position: relative;
    font-family: "Open Sans", sans-serif;
  }
  .card {
    position: absolute;
    width: 540px;
    height: 309px;
    background: var(--paper);
    overflow: hidden;
    box-shadow: 0 6px 18px rgba(0,0,0,0.12);
  }
  .card-back { left: 40px; top: 245px; }
  .card-front { left: 620px; top: 245px; }
  .card-shapes { position: absolute; inset: 0; width: 100%; height: 100%; }

  /* Back side */
  .brand {
    position: absolute;
    left: 0; right: 0; top: 92px;
    display: flex; align-items: center; justify-content: center; gap: 14px;
  }
  .brand-dot {
    width: 34px; height: 34px; border-radius: 50%;
    background: var(--gold);
    flex: none;
  }
  .brand-name {
    font-family: "Playfair Display", serif;
    font-size: 40px;
    color: var(--brown);
    letter-spacing: 0.5px;
  }
  .agent-line {
    position: absolute;
    left: 100px; right: 70px; top: 158px;
    display: flex; align-items: center; gap: 12px;
  }
  .agent-rule { flex: 1; height: 1px; background: var(--brown); }
  .agent-name {
    font-family: "Open Sans", sans-serif;
    font-weight: 600;
    font-size: 15px;
    color: var(--brown);
  }
  .partner-badge {
    width: 34px; height: 26px;
    background: var(--brown);
    flex: none;
  }
  .tagline {
    font-family: "Open Sans", sans-serif;
    font-weight: 400;
    font-size: 11px;
    color: var(--muted);
  }
  .back-tagline {
    position: absolute; left: 0; right: 0; top: 186px;
    text-align: center;
  }
  .web-box {
    position: absolute;
    left: 60px; top: 228px;
    border: 1px solid #b9a88a;
    padding: 5px 16px;
    font-size: 14px;
    color: var(--ink);
  }

  /* Front side */
  .name-block { position: absolute; left: 22px; top: 22px; }
  .name-bar {
    position: absolute; left: 0; top: 2px;
    width: 8px; height: 40px; background: var(--brown);
  }
  .name {
    margin-left: 16px;
    font-family: "Encode Sans Condensed", sans-serif;
    font-size: 36px; line-height: 1;
    color: var(--brown);
  }
  .name strong { font-weight: 700; }
  .name span { font-weight: 500; }
  .role {
    margin-left: 16px; margin-top: 3px;
    font-size: 12px; color: var(--ink);
  }
  .name-rule {
    margin-left: 120px; margin-top: 2px;
    width: 90px; height: 2px; background: var(--gold);
  }
  .contact {
    position: absolute; left: 26px; top: 140px;
    list-style: none;
    font-size: 14px; color: var(--ink);
  }
  .contact li { display: flex; align-items: center; gap: 7px; line-height: 21px; }
  .contact li.phone { font-weight: 600; font-size: 16px; }
  .contact svg { width: 11px; height: 11px; fill: var(--ink); flex: none; }
  .front-logo {
    position: absolute; left: 350px; top: 118px; width: 170px;
    display: flex; flex-direction: column; align-items: center; gap: 8px;
  }
  .front-logo .brand-dot { width: 40px; height: 40px; }
  .front-logo .agent-name { font-size: 20px; }
  .front-logo .tagline { margin-top: -4px; }
</style>
</head>
<body>

  <section class="card card-back" aria-label="Card back">
    <svg class="card-shapes" viewBox="0 0 540 309" aria-hidden="true">
      <path fill="var(--brown)" d="M0,0 L150,0 C95,18 40,50 0,100 Z"/>
      <path fill="var(--brown)" d="M540,309 L370,309 C440,300 500,270 540,220 Z"/>
    </svg>
    <div class="brand">
      <span class="brand-dot"></span>
      <span class="brand-name">Cedar Lark Homes</span>
    </div>
    <div class="agent-line">
      <span class="agent-rule"></span>
      <span class="agent-name">Maren Quill</span>
      <span class="agent-rule"></span>
      <span class="partner-badge" role="img" aria-label="Brindley Vance partner badge"></span>
    </div>
    <p class="tagline back-tagline">Rooted in Trust</p>
    <div class="web-box">www.cedarlarkhomes.example</div>
  </section>

  <section class="card card-front" aria-label="Card front">
    <svg class="card-shapes" viewBox="0 0 540 309" aria-hidden="true">
      <path fill="var(--gold)" d="M0,118 C90,96 160,118 200,170 C250,236 330,286 540,250 L540,309 L0,309 Z"/>
      <path fill="var(--brown)" d="M55,104 C120,86 165,108 190,152 C155,120 115,110 55,114 Z"/>
      <path fill="var(--paper)" d="M320,248 C380,300 470,298 540,282 L540,292 C460,306 375,300 320,248 Z"/>
      <path fill="var(--gold-light)" d="M540,292 C470,305 390,302 330,258 C400,300 470,306 540,300 Z"/>
      <path fill="var(--brown)" d="M410,258 C460,244 505,232 540,214 L540,224 C505,240 460,252 410,262 Z"/>
    </svg>
    <div class="name-block">
      <span class="name-bar"></span>
      <div class="name"><strong>MAREN</strong> <span>QUILL</span></div>
      <div class="role">Associate Broker</div>
      <div class="name-rule"></div>
    </div>
    <ul class="contact">
      <li class="phone">
        <svg viewBox="0 0 24 24"><path d="M6.6 10.8a15 15 0 0 0 6.6 6.6l2.2-2.2a1 1 0 0 1 1-.25 11.4 11.4 0 0 0 3.6.6 1 1 0 0 1 1 1V20a1 1 0 0 1-1 1A17 17 0 0 1 3 4a1 1 0 0 1 1-1h3.5a1 1 0 0 1 1 1c0 1.25.2 2.45.6 3.6a1 1 0 0 1-.25 1z"/></svg>
        730-418-5093
      </li>
      <li>
        <svg viewBox="0 0 24 24"><path d="M2 5h20v14H2z M2 5l10 8 10-8" fill="none" stroke="#1e1a14" stroke-width="2.4"/></svg>
        marenquill@cedarlarkhomes.example
      </li>
      <li>
        <svg viewBox="0 0 24 24"><circle cx="12" cy="12" r="9" fill="none" stroke="#1e1a14" stroke-width="2.4"/><path d="M3 12h18M12 3c-4 5-4 13 0 18M12 3c4 5 4 13 0 18" fill="none" stroke="#1e1a14" stroke-width="2"/></svg>
        www.cedarlarkhomes.example
      </li>
    </ul>
    <div class="front-logo">
      <span class="brand-dot"></span>
      <span class="agent-name">Maren Quill</span>
      <p class="tagline">Rooted in Trust</p>
    </div>
  </section>

</body>
</html>
```